Coralwake Trail Outings is an Exciting Water and Land Excursions business that needs a website.

We need a website for our company. We are based in Bimini Bahamas and we sell land and sea excursions. We sell Private boat Charters, Reef Shark Snorkeling, Corvella Shipwreck Snorkeling, Stingray feeding adventures, Dolphin Tours, Sunset Cruises, Scuba Diving, Offshore Fishing, Reef Fishing, Flats Backwater Fishing, Party Island Cruise, Island Land Party Bicycle Tours, Jet Ski Tours, Guided Kayak Tours, Beach Chairs/Umbrella Rentals, Cabana Rentals, Jet Ski Rentals, Kayak Rentals, Paddle Board Rentals, Water Hammock Rentals, and Paint by the Sea Excursion

The home page will have the following tabs:
Adventures
Watersports
Photos
Alcohol
START YOUR ADVENTURE - Booking button
The adventures

We are currently using peekpro for our reservation system and that will need to be integrated with our website along with zenfolio or a similar app for purchase of photos.
Updates

Need extra days to review

Target Market(s)

Our target market are tourists

Industry/Entity Type

Tourism

Coding

Coded - Design and coding required

Font styles to use
Sans Serif

Colors
0094D4
00A9DD
6FCCEA
C7EBF8
E9F6FB

Requirements
Must have
• The website must be in wordpress so we can add our external reservation system
Nice to have
• We need to have big photos and a lot of photos

```html
<!DOCTYPE html>
<html lang="en">
<head>
<meta charset="utf-8">
<title>Contact – Coralwake Trail Outings</title>
<link href="https://fonts.googleapis.com/css2?family=Barlow+Condensed:wght@700&family=Hind:wght@400;500;600&display=swap" rel="stylesheet">
<style>
:root{
  --blue:#211fa0;
  --green:#39c338;
  --dark:#0c0b1f;
  --ink:#2a2a3a;
  --muted:#5d5d6e;
  --line:#c9c9cf;
  --foot-text:#b4b4c8;
  --white:#fff;
}
*{box-sizing:border-box;margin:0;padding:0}
html,body{width:834px;height:1200px;overflow:hidden}
body{position:relative;background:var(--white);font-family:"Hind",sans-serif;color:var(--ink)}
.abs{position:absolute}
.topbar{left:0;top:0;width:834px;height:27px;background:var(--blue);color:var(--white);font-size:11px}
.dot{position:absolute;width:12px;height:12px;border-radius:50%;background:var(--white)}
.topbar .contact-item{position:absolute;top:6px;display:flex;align-items:center;gap:7px;line-height:14px}
.topbar .sep{position:absolute;left:614px;top:7px;width:1px;height:13px;background:#8e8cd6}
.nav{left:0;top:27px;width:834px;height:56px;background:var(--white)}
.brand{position:absolute;left:56px;top:19px;display:flex;align-items:center;gap:6px;font-weight:600;font-size:12.5px;color:var(--blue);letter-spacing:.3px}
.brand .mark{width:14px;height:14px;background:var(--green)}
.menu{position:absolute;left:283px;top:20px;display:flex;gap:13px;font-size:11.5px;font-weight:500;color:#4a4a5a}
.menu .active{color:var(--blue);position:relative}
.menu .active::after{content:"";position:absolute;left:15px;top:18px;width:14px;height:2px;border-top:2px dotted var(--blue)}
.book{position:absolute;left:661px;top:13px;width:105px;height:30px;background:var(--green);color:var(--white);font-weight:600;font-size:10.5px;letter-spacing:.5px;display:flex;align-items:center;justify-content:center}
.hero{left:0;top:83px;width:834px;height:197px;background:linear-gradient(180deg,#4c6a4e 0%,#7d8f74 35%,#cfd1cc 60%,#d8d9d6 100%)}
.title{left:55px;top:338px;font-family:"Barlow Condensed",sans-serif;font-weight:700;font-size:33px;color:#1c1b33;line-height:1}
.title-rule{left:55px;top:381px;width:44px;height:3px;background:var(--blue)}
.intro{left:56px;top:400px;width:290px;font-size:12px;line-height:22px;color:#3a3a48}
.info-card{left:56px;top:478px;width:261px;height:302px;background:var(--green);box-shadow:0 8px 18px rgba(0,0,0,.18);color:var(--white)}
.info-row{position:absolute;left:16px;display:flex;gap:14px}
.ibox{width:39px;height:39px;background:var(--white);display:flex;align-items:center;justify-content:center;flex:none}
.info-row p{font-size:12.5px;line-height:21px;margin-top:-3px}
.social-label{position:absolute;left:15px;top:216px;font-weight:600;font-size:12px}
.social-line{position:absolute;left:100px;top:239px;width:145px;height:1px;background:rgba(255,255,255,.8)}
.social-dots{position:absolute;left:16px;top:265px;display:flex;gap:14px}
.social-dots span{width:11px;height:11px;border-radius:50%;background:var(--white)}
.field{position:absolute;border:1px solid var(--line);font-size:12px;color:#6a6a78;padding:10px 12px;line-height:14px}
.send{left:655px;top:744px;width:111px;height:36px;background:var(--green);color:var(--white);font-weight:600;font-size:11px;letter-spacing:.5px;display:flex;align-items:center;justify-content:center;box-shadow:0 4px 8px rgba(0,0,0,.12)}
.footer-bg{left:0;top:834px;width:834px;height:366px}
.fhead{position:absolute;top:938px;font-family:"Barlow Condensed",sans-serif;font-weight:700;font-size:19px;color:var(--white);line-height:1}
.ftext{position:absolute;font-size:11.5px;line-height:22px;color:var(--foot-text)}
.flinks{list-style:none;position:absolute;top:973px;font-size:11.5px;line-height:22.2px;color:var(--foot-text)}
.fdots{position:absolute;left:56px;top:1075px;display:flex;gap:17px}
.fdots span{width:11px;height:11px;border-radius:50%;background:var(--white)}
.cbox{position:absolute;left:591px;width:32px;height:32px;background:var(--green);display:flex;align-items:center;justify-content:center}
.copy{left:0;top:1160px;width:834px;text-align:center;font-size:9.5px;letter-spacing:.3px;color:#a0a0b8}
</style>
</head>
<body>

<header class="abs topbar">
  <span class="dot" style="left:57px;top:7px"></span>
  <span class="dot" style="left:88px;top:7px"></span>
  <span class="dot" style="left:116px;top:7px"></span>
  <div class="contact-item" style="left:500px">
    <svg width="11" height="11" viewBox="0 0 24 24"><path fill="#fff" d="M6.6 10.8a15.1 15.1 0 0 0 6.6 6.6l2.2-2.2a1 1 0 0 1 1-.25 11.4 11.4 0 0 0 3.6.57 1 1 0 0 1 1 1V20a1 1 0 0 1-1 1A17 17 0 0 1 3 4a1 1 0 0 1 1-1h3.5a1 1 0 0 1 1 1c0 1.25.2 2.45.57 3.57a1 1 0 0 1-.25 1z"/></svg>
    123-456-7890
  </div>
  <span class="sep"></span>
  <div class="contact-item" style="left:636px">
    <svg width="12" height="12" viewBox="0 0 24 24"><path fill="#fff" d="M2 9l10-7 10 7v12H2z"/><path fill="none" stroke="#211fa0" stroke-width="2" d="M6 11l6 4 6-4"/></svg>
    info@coralwaketrail.com
  </div>
</header>

<nav class="abs nav">
  <div class="brand"><span class="mark"></span>Coralwake Trail Outings</div>
  <div class="menu">
    <span>Home</span><span>Our Adventures</span><span>Beach Fun</span><span>Alcohol Delivery</span><span class="active">Contact</span>
  </div>
  <div class="book">BOOK NOW</div>
</nav>

<div class="abs hero" role="img" aria-label="Aerial photo of the beach with rental kayaks, huts and palm trees"></div>

<h1 class="abs title">CONTACT</h1>
<div class="abs title-rule"></div>
<p class="abs intro">Quis nostrud exercitation ullamco laboris nisi ut aliquip ex ea commodo consequat.</p>

<section class="abs info-card">
  <div class="info-row" style="top:24px">
    <div class="ibox"><svg width="13" height="15" viewBox="0 0 24 28"><path fill="#211fa0" d="M12 0a10 10 0 0 0-10 10c0 7.5 10 18 10 18s10-10.5 10-18A10 10 0 0 0 12 0zm0 14a4 4 0 1 1 0-8 4 4 0 0 1 0 8z"/></svg></div>
    <p>Address:<br>et accusamus et iusto odio dignissimos</p>
  </div>
  <div class="info-row" style="top:101px">
    <div class="ibox"><svg width="14" height="14" viewBox="0 0 24 24"><path fill="#211fa0" d="M6.6 10.8a15.1 15.1 0 0 0 6.6 6.6l2.2-2.2a1 1 0 0 1 1-.25 11.4 11.4 0 0 0 3.6.57 1 1 0 0 1 1 1V20a1 1 0 0 1-1 1A17 17 0 0 1 3 4a1 1 0 0 1 1-1h3.5a1 1 0 0 1 1 1c0 1.25.2 2.45.57 3.57a1 1 0 0 1-.25 1z"/></svg></div>
    <p>Phone No:<br>123-456-7890</p>
  </div>
  <div class="info-row" style="top:163px">
    <div class="ibox"><svg width="15" height="15" viewBox="0 0 24 24"><path fill="#211fa0" d="M2 9l10-7 10 7v12H2z"/><path fill="none" stroke="#fff" stroke-width="2" d="M6 11l6 4 6-4"/></svg></div>
    <p>Email Address:<br>info@coralwaketrail.com</p>
  </div>
  <div class="social-label">Social Media</div>
  <div class="social-line"></div>
  <div class="social-dots"><span></span><span></span><span></span></div>
</section>

<div class="field" style="left:335px;top:478px;width:211px;height:36px">Name</div>
<div class="field" style="left:555px;top:478px;width:211px;height:36px">Email</div>
<div class="field" style="left:335px;top:523px;width:211px;height:36px">Phone</div>
<div class="field" style="left:555px;top:523px;width:211px;height:36px">Subject</div>
<div class="field" style="left:335px;top:568px;width:431px;height:164px">Message</div>
<div class="abs send">SEND NOW</div>

<svg class="abs footer-bg" width="834" height="366" viewBox="0 0 834 366"><path fill="#0c0b1f" d="M0 0L834 68V366H0z"/></svg>

<h2 class="fhead" style="left:56px">ABOUT US</h2>
<p class="ftext" style="left:56px;top:973px;width:240px">Lorem ipsum dolor sit amet, consecteou adipisicings elit, sed do eiusmod tempor al incididunt ut labore et dolore magna aute aliquat enim ad minim</p>
<div class="fdots"><span></span><span></span><span></span></div>

<h2 class="fhead" style="left:324px">QUICK LINKS</h2>
<ul class="flinks" style="left:325px">
  <li>Our locations</li><li>Gift shop</li><li>Adventure Center</li><li>Corporate</li><li>Kayak Beach</li><li>Paradise Beach</li>
</ul>
<ul class="flinks" style="left:449px">
  <li>Where to Dock</li><li>Halcyon Bay Marina</li><li>Where to Stay</li><li>Seabright Cove Resort</li><li>How to get here</li><li>Skylark Isles Air</li><li>Tidewind Ferry</li>
</ul>

<h2 class="fhead" style="left:591px">CONTACT INFORMATION</h2>
<div class="cbox" style="top:975px"><svg width="11" height="13" viewBox="0 0 24 28"><path fill="#fff" d="M12 0a10 10 0 0 0-10 10c0 7.5 10 18 10 18s10-10.5 10-18A10 10 0 0 0 12 0zm0 14a4 4 0 1 1 0-8 4 4 0 0 1 0 8z"/></svg></div>
<p class="ftext" style="left:639px;top:969px;line-height:19.5px">labore et dolore magna<br>aute eniam aliqu</p>
<div class="cbox" style="top:1020px"><svg width="12" height="12" viewBox="0 0 24 24"><path fill="#fff" d="M6.6 10.8a15.1 15.1 0 0 0 6.6 6.6l2.2-2.2a1 1 0 0 1 1-.25 11.4 11.4 0 0 0 3.6.57 1 1 0 0 1 1 1V20a1 1 0 0 1-1 1A17 17 0 0 1 3 4a1 1 0 0 1 1-1h3.5a1 1 0 0 1 1 1c0 1.25.2 2.45.57 3.57a1 1 0 0 1-.25 1z"/></svg></div>
<p class="ftext" style="left:639px;top:1014px;line-height:19.5px">Phone:<br>123-456-7890</p>
<div class="cbox" style="top:1066px"><svg width="13" height="13" viewBox="0 0 24 24"><path fill="#fff" d="M2 9l10-7 10 7v12H2z"/><path fill="none" stroke="#39c338" stroke-width="2" d="M6 11l6 4 6-4"/></svg></div>
<p class="ftext" style="left:639px;top:1059px;line-height:19.5px">Email:<br>info@coralwaketrail.com</p>

<p class="abs copy">COPYRIGHT © 2022 CORALWAKE TRAIL OUTINGS. ALL RIGHTS RESERVED.</p>

</body>
</html>
```